Brightwell Systems - Company Overview Brochure

We would like a single page A4 Brochure to give to new potential customers to provide a quick overview of our company. This will be used in presales meetings.

We have included the content we would like on the brochure under "Brightwell Systems Marketing Brochure.docx".

We have included two other designs "timebundleterms v4.pdf and Brightwell Public Cloud Plans.pdf" which shows similar marketing brochures we have. We would like these designs to have the same Brightwell Blue and "Specialised Technology Consultancy firm" theme.

Target Market(s)

Technology Sector

Industry/Entity Type

Information Technology

Colors
0054AA
0677BA
7BADD7
CADEEF
E8F1F8

Requirements
Must have
• "Innovative Tech Company Theme".

```html
<!DOCTYPE html>
<html lang="en">
<head>
<meta charset="utf-8">
<title>Brightwell Systems – Company Overview</title>
<link href="https://fonts.googleapis.com/css2?family=Archivo:ital,wght@0,300;0,400;0,600;0,800;1,700;1,800&family=Manrope:wght@400;500;700&display=swap" rel="stylesheet">
<style>
:root{
  --brand-deep:#0054AA;
  --brand-mid:#0677BA;
  --brand-soft:#7BADD7;
  --brand-pale:#CADEEF;
  --brand-mist:#E8F1F8;
  --navy:#0B1F5C;
  --night:#06144A;
  --white:#ffffff;
  --stage:#0d0d0d;
}
*{box-sizing:border-box;margin:0;padding:0}
html,body{width:1200px;height:3231px;overflow:hidden;background:var(--stage)}
.brochure{
  position:absolute;left:150px;top:980px;width:900px;height:1270px;overflow:hidden;
  background:linear-gradient(160deg,#0a3f8f 0%,#0a4fa6 40%,var(--brand-deep) 70%,#0b3d95 100%);
  font-family:"Manrope",sans-serif;color:var(--white);
}
.photo-team{position:absolute;left:430px;top:0;width:470px;height:760px;
  background:linear-gradient(180deg,#1f4f8e 0%,#2a68b0 35%,rgba(10,79,166,.6) 75%,rgba(10,79,166,0) 100%)}
.photo-servers{position:absolute;left:0;top:180px;width:460px;height:360px;
  background:linear-gradient(90deg,rgba(40,90,160,.7),rgba(20,70,150,.2) 80%,rgba(10,79,166,0))}
.header-band{position:absolute;left:0;top:0;width:900px;height:180px}
.brand-name{position:absolute;left:52px;top:70px;display:flex;align-items:center;gap:16px;
  font-family:"Archivo",sans-serif;font-weight:800;font-size:30px;color:var(--brand-deep);letter-spacing:.5px}
.brand-name .mark{width:26px;height:26px;background:var(--brand-deep)}
.headline{position:absolute;left:58px;top:238px;font-family:"Archivo",sans-serif;line-height:1.08;font-size:62px;letter-spacing:.5px}
.headline .strong{font-weight:600;display:block}
.headline .light{font-weight:300;display:block}
.intro{position:absolute;left:493px;top:255px;width:380px;font-size:19px;line-height:1.3;font-weight:400}
.intro strong{font-weight:700;display:block}
.grid{position:absolute;left:0;top:0;width:900px;height:1270px}
.hex-label{font-family:"Manrope",sans-serif;font-size:18px;font-weight:500;fill:var(--white)}
.hex-title{font-family:"Archivo",sans-serif;font-style:italic;font-weight:800;fill:var(--brand-deep)}
.section{position:absolute;font-size:14.5px;line-height:1.15}
.section h2{font-family:"Archivo",sans-serif;font-style:italic;font-weight:600;font-size:19px;color:var(--brand-pale);margin-bottom:6px;letter-spacing:.3px}
.section p{margin-bottom:16px}
.section h3{font-size:14.5px;font-weight:700;margin-bottom:2px}
.commitment{left:50px;top:795px;width:300px}
.policy{left:380px;top:793px;width:246px}
.slogan{position:absolute;left:0;top:0}
.slogan-text{position:absolute;left:352px;top:1132px;width:548px;text-align:center;
  font-family:"Archivo",sans-serif;font-style:italic;font-weight:800;font-size:37px;color:var(--brand-deep)}
.footer{position:absolute;left:0;top:1193px;width:900px;height:77px;background:var(--night);
  padding:22px 45px;font-size:11.5px;line-height:1.45}
</style>
</head>
<body>
<main class="brochure">
  <div class="photo-team" role="img" aria-label="Photo of two technology consultants reviewing a tablet"></div>
  <div class="photo-servers" role="img" aria-label="Faint photo of a server room"></div>

  <svg class="header-band" viewBox="0 0 900 180" aria-hidden="true">
    <polygon points="0,0 477,0 433,180 0,180" fill="#ffffff"/>
  </svg>
  <div class="brand-name"><span class="mark"></span>Brightwell Systems</div>

  <h1 class="headline"><span class="strong">SPECIALISED</span><span class="light">CONSULTING</span></h1>
  <p class="intro"><strong>Brightwell Systems</strong>is a Technology Consulting Company based in Perth, Western Australia, which offers customers tailored technical solutions for a range of products.</p>

  <svg class="grid" viewBox="0 0 900 1270">
    <defs>
      <polygon id="hx" points="0,-100 86.6,-50 86.6,50 0,100 -86.6,50 -86.6,-50"/>
      <linearGradient id="streak" x1="0" y1="1" x2="1" y2="0">
        <stop offset="0" stop-color="#7BADD7" stop-opacity="0"/>
        <stop offset="1" stop-color="#CADEEF" stop-opacity=".55"/>
      </linearGradient>
    </defs>
    <polygon points="0,1190 880,860 890,870 0,1210" fill="url(#streak)"/>
    <polygon points="230,1190 560,1000 520,1190" fill="#0d3a8a" opacity=".35"/>

    <g fill="none" stroke="#CADEEF" stroke-width="1.6" opacity=".9">
      <use href="#hx" x="0" y="508"/>
      <use href="#hx" x="352" y="508"/>
      <use href="#hx" x="528" y="508"/>
      <use href="#hx" x="901" y="508"/>
      <use href="#hx" x="88" y="658"/>
      <use href="#hx" x="264" y="658"/>
      <use href="#hx" x="440" y="658"/>
      <use href="#hx" x="637" y="658"/>
      <use href="#hx" x="813" y="658"/>
      <use href="#hx" x="725" y="808"/>
      <use href="#hx" x="901" y="808"/>
      <use href="#hx" x="813" y="958"/>
    </g>
    <use href="#hx" x="176" y="508" fill="#ffffff"/>
    <use href="#hx" x="725" y="508" fill="#ffffff"/>

    <g fill="#ffffff">
      <circle cx="352" cy="608" r="6"/><circle cx="176" cy="708" r="6"/>
      <circle cx="528" cy="708" r="5"/><circle cx="725" cy="608" r="6"/>
      <circle cx="637" cy="758" r="5"/><circle cx="813" cy="858" r="6"/>
    </g>

    <text class="hex-title" x="98" y="505" font-size="54">IT</text>
    <text class="hex-title" x="98" y="543" font-size="28">SERVICES</text>
    <text class="hex-title" x="647" y="492" font-size="22">ELECTRONIC</text>
    <text class="hex-title" x="647" y="517" font-size="22">SECURITY &amp;</text>
    <text class="hex-title" x="647" y="538" font-size="16">COMMUNICATIONS</text>

    <g fill="none" stroke="#7BADD7" stroke-width="2.2" stroke-linecap="round" stroke-linejoin="round">
      <circle cx="338" cy="468" r="11"/><circle cx="366" cy="488" r="11"/>
      <path d="M350 458h18l-5-5M356 498h-18l5 5"/>
      <path d="M62 610v46h30v-46zM70 620h4M80 620h4M70 632h4M80 632h4"/>
      <path d="M98 628l14 6v10c0 8-6 12-14 15-8-3-14-7-14-15v-10z"/>
      <circle cx="264" cy="612" r="22"/><circle cx="264" cy="606" r="7"/><path d="M252 626c3-8 21-8 24 0"/>
      <rect x="416" y="600" width="44" height="34" rx="3"/><path d="M416 610h44M432 618l-6 6 6 6M444 618l6 6-6 6"/><circle cx="462" cy="598" r="8"/>
      <path d="M608 618l36-10 6 14-36 10zM614 630l-4 14h-14M596 636v16"/><circle cx="660" cy="640" r="10"/>
      <path d="M786 605h54M796 595v20M806 592v26M816 595v20M826 598v14"/>
      <path d="M715 775h20v20h-20zM718 775l-14-22M725 775v-26M732 775l14-22M721 775l-6-28M729 775l6-28"/>
      <path d="M813 948l-10 32M813 948l10 32M806 966h14"/><circle cx="813" cy="944" r="4"/>
      <path d="M798 932a20 20 0 0 0 0 26M828 932a20 20 0 0 1 0 26M790 924a32 32 0 0 0 0 42M836 924a32 32 0 0 1 0 42"/>
    </g>

    <g class="hex-label" text-anchor="middle">
      <text x="352" y="526">Project</text><text x="352" y="546">Integration</text>
      <text x="88" y="682">Enterprise</text><text x="88" y="702">Security</text>
      <text x="264" y="682">Managed</text><text x="264" y="702">Services</text>
      <text x="440" y="682">Software</text><text x="440" y="702">Development</text>
      <text x="637" y="702">CCTV</text>
      <text x="813" y="676">Integrated</text><text x="813" y="696">Electronic</text><text x="813" y="716">Security</text>
      <text x="725" y="832">Structure</text><text x="725" y="852">Cabling &amp;</text><text x="725" y="872">Fibre Optics</text>
      <text x="813" y="1003">Wireless</text><text x="813" y="1023">Communications</text>
    </g>

    <polygon class="slogan" points="368,1130 900,1130 900,1193 352,1193" fill="#ffffff"/>
  </svg>

  <section class="section commitment">
    <h2>OUR COMMITMENT</h2>
    <p>Our commitment to you is to do things right the first time while being fair but cost-effective. If you're looking for the cheapest consultants, Brightwell may not be the right fit for you.</p>
    <p>We are a specialised consultancy firm that offers tailored solutions to government and the enterprise sector with some of Perth's best consultants.</p>
    <p>In areas such as cybersecurity and business continuity, it pays to get it done correctly the first time in alignment with vendor best practices. There are many ways of doing things in the technology field, and only after understanding all methods of achieving an outcome can you recommend the best solution in alignment with best practices.</p>
  </section>

  <section class="section policy">
    <h2>OUR POLICY</h2>
    <h3>Be Fair</h3>
    <p>“At Brightwell we believe that both parties benefit when pricing is fair. If margins are too low, we may sacrifice service quality, and this ultimately harms our brand. If margins are too high, our customers have an incentive to seek alternative providers, and this compromises our growth and damages client relationships.”</p>
    <h3>Be Cost-Effective</h3>
    <p>“At Brightwell we believe that it is possible to deliver both high quality at a fair cost, by providing services that are intelligent and efficient.”</p>
  </section>

  <p class="slogan-text">“Do it Once, Do it Right”</p>

  <footer class="footer">All goods and services provided by Brightwell are provided in accordance with our Standard Terms and Conditions available at<br>https://www.brightwellsystems.com.au/t&amp;c</footer>
</main>
</body>
</html>
```